Company Profile Redesign Format Using InDesign

We have prepared a company profile using MS word, we would like a more professionally designed document designed and packaged in InDesign. The content should not require any amendments - but we are open to any suggestions. Also the photographs should be fine. Other graphics, again we are open to suggestion.

Target Market(s)

Energy Companies

Industry/Entity Type

Construction

Colors
ec1f27

Requirements
Nice to have
• A more modern and professional approach

```html
<!DOCTYPE html>
<html lang="en">
<head>
<meta charset="utf-8">
<title>Corvane Group Company Profile – Energy Performance Certificates</title>
<link href="https://fonts.googleapis.com/css2?family=Source+Sans+3:wght@400;600;700&display=swap" rel="stylesheet">
<style>
  :root {
    --brand-red: #ec1f27;
    --heading-band: #f6ad94;
    --ink: #231f20;
    --muted: #3a3a3a;
    --paper: #ffffff;
    --art-light: #f7f7f7;
    --art-mid: #e6e6e6;
  }
  * { margin: 0; padding: 0; box-sizing: border-box; }
  html, body { width: 853px; height: 1200px; overflow: hidden; background: var(--paper); }
  .page {
    position: relative;
    width: 853px;
    height: 1200px;
    background: var(--paper);
    font-family: "Source Sans 3", "Myriad Pro", Arial, sans-serif;
    color: var(--ink);
    overflow: hidden;
  }
  .running-head { position: absolute; top: 0; left: 0; width: 853px; height: 32px; }
  .running-head-title {
    position: absolute; top: 5px; left: 61px;
    color: var(--paper); font-size: 17px; font-weight: 400;
  }
  .section-title {
    position: absolute; top: 107px; left: 60px; width: 724px; height: 27px;
    background: var(--heading-band);
    font-size: 18.5px; font-weight: 700; line-height: 27px; padding-left: 6px;
  }
  .body-copy {
    position: absolute; left: 60px; width: 724px;
    font-size: 14.8px; line-height: 19.2px; color: var(--ink);
  }
  .body-copy p + p { margin-top: 9px; }
  .intro { top: 150px; }
  .closing { top: 867px; }
  .illustration {
    position: absolute; top: 318px; left: 78px; width: 712px; height: 492px;
    background: radial-gradient(ellipse at 50% 50%, var(--art-mid) 0%, var(--art-light) 55%, var(--paper) 85%);
  }
  .page-number {
    position: absolute; top: 907px; left: 0; width: 33px; height: 29px;
    background: var(--brand-red); color: var(--paper);
    font-size: 13px; font-weight: 700; text-align: center; line-height: 29px;
  }
  .footer-rule { position: absolute; top: 1120px; left: 60px; width: 724px; height: 1px; background: var(--brand-red); }
  .footer-details {
    position: absolute; top: 1126px; left: 60px; width: 724px;
    text-align: center; font-size: 10.4px; line-height: 15px; color: var(--muted);
  }
  .footer-details strong { font-weight: 700; color: var(--ink); }
  .footer-details span + span { margin-left: 10px; }
  .bottom-band { position: absolute; bottom: 0; left: 0; width: 853px; height: 20px; background: var(--brand-red); }
</style>
</head>
<body>
<div class="page">
  <header class="running-head">
    <svg width="853" height="32" viewBox="0 0 853 32" aria-hidden="true">
      <polygon points="0,0 290,0 308,28 0,28" fill="var(--brand-red)"/>
      <rect x="0" y="27" width="853" height="2" fill="var(--brand-red)"/>
    </svg>
    <span class="running-head-title">Corvane Group Company Profile</span>
  </header>

  <h1 class="section-title">Energy Performance Certificates</h1>

  <section class="body-copy intro">
    <p>All domestic and commercial buildings in the UK available to buy or rent must have an Energy Performance Certificate (EPC). An energy performance survey helps homeowners to identify ways to save money on their energy bills and improve the comfort of their home.</p>
    <p>As part of the assessment to check whether customer’s properties are eligible for free insulation, gas boiler or any other energy saving measures, the property owner will require an Energy Performance Certificate (EPC) for the property. Corvane will complete this free of charge whilst assessing and surveying the property.</p>
  </section>

  <div class="illustration" role="img" aria-label="Illustration of a house with a red roof beside an A to G energy efficiency rating chart, resting on rolled architectural plans"></div>

  <section class="body-copy closing">
    <p>The EPC will also state what the energy-efficiency rating could be if improvements are made, and highlights cost-effective ways to achieve a better rating. Even if the property is rented, some improvements noted on the EPC may be worth implementing, such as switching to more energy-efficient light bulbs. EPCs are valid for 10 years from issue.</p>
    <p>As from the 1st April 2018 there will be a requirement for any properties rented out in the private rented sector to normally have a minimum energy performance rating of E on an Energy Performance Certificate (EPC).</p>
  </section>

  <div class="page-number">6</div>

  <footer>
    <div class="footer-rule"></div>
    <div class="footer-details">
      <div><strong>Corvane Group Limited</strong>, Riverside Enterprise Hub, Mill Lane, Hartlepool, TS24 8QW</div>
      <div><span>t: 0191 000 4827</span><span>e: hello@corvane.co.uk</span><span>www.corvane.co.uk</span><span>Company No. 01234567</span><span>VAT No: 100 2345 67</span></div>
    </div>
    <div class="bottom-band"></div>
  </footer>
</div>
</body>
</html>
```